pathology learning flashcard template graphic design .

Creative designs for 2 sides of the flashcards to include colorful sectioning and font sizes that will make it easy to use in studying.

```html
<!DOCTYPE html>
<html lang="en">
<head>
<meta charset="utf-8">
<title>Gastrointestinal Pathology Flashcard 0001</title>
<link href="https://fonts.googleapis.com/css2?family=Carlito:ital,wght@0,400;0,700;1,400;1,700&family=Titillium+Web:ital,wght@0,200;0,300;1,700;1,900&family=Noto+Serif:wght@700&display=swap" rel="stylesheet">
<style>
  :root{
    --navy:#17284f;
    --navy-deep:#0f1b3a;
    --pink:#ec1b78;
    --orange:#f26a2a;
    --coral:#ef4f52;
    --peach:#f9bfaa;
    --paper:#f1f1f3;
    --white:#ffffff;
    --ink:#1b1b1b;
  }
  *{margin:0;padding:0;box-sizing:border-box;}
  html,body{width:912px;height:1200px;overflow:hidden;background:var(--white);}
  .canvas{position:relative;width:912px;height:1200px;font-family:"Carlito",Calibri,sans-serif;}
  .art{position:absolute;left:0;top:0;}
  .front-text,.back-text{position:absolute;color:var(--white);}
  .watermark{position:absolute;left:409px;top:100px;font-family:"Titillium Web",sans-serif;font-weight:900;font-style:italic;font-size:122px;line-height:1;color:rgba(255,255,255,.07);letter-spacing:-2px;white-space:nowrap;}
  .card-subject{position:absolute;left:396px;top:186px;font-family:"Titillium Web",sans-serif;font-weight:700;font-style:italic;font-size:35px;line-height:1;color:var(--pink);letter-spacing:-.5px;}
  .case-id{position:absolute;left:396px;top:244px;font-family:"Titillium Web",sans-serif;font-weight:200;font-size:28.5px;line-height:1;color:var(--orange);white-space:nowrap;}
  .case-stem{position:absolute;left:396px;top:278px;font-style:italic;font-size:16.2px;line-height:20.8px;color:#e9ecf4;white-space:nowrap;}
  .divider{position:absolute;left:396px;top:498px;width:465px;height:2px;background:var(--orange);}
  .options{position:absolute;left:396px;top:511px;font-family:"Titillium Web",sans-serif;font-style:italic;font-weight:700;font-size:15.5px;line-height:21px;color:var(--white);}
  .options .letter{color:var(--orange);font-weight:300;}
  .options span.opt{margin-right:8px;}

  .topic-title{left:136px;top:696px;font-family:"Titillium Web",sans-serif;font-weight:700;font-style:italic;font-size:26px;line-height:1;}
  .section{font-style:italic;font-size:11.6px;line-height:15.5px;}
  .section b{font-family:"Titillium Web",sans-serif;font-weight:700;font-size:14px;}
  .label-block{display:block;font-family:"Titillium Web",sans-serif;font-weight:700;font-size:14px;line-height:18px;}
  .definition{left:137px;top:732px;width:280px;}
  .etiology{left:134px;top:793px;width:300px;font-size:11.8px;line-height:17.5px;}
  .symptoms{left:427px;top:700px;width:330px;}
  .diagnosis{left:429px;top:782px;width:340px;}
  .treatment{left:140px;top:893px;width:600px;font-size:11.8px;line-height:17.5px;}

  .answer-box{position:absolute;left:131px;top:953px;width:657px;height:153px;background:var(--peach);border:3px solid var(--navy);border-radius:14px 6px 24px 4px;padding:8px 14px 0 14px;color:var(--ink);}
  .answer-title{font-family:"Titillium Web",sans-serif;font-weight:700;font-style:italic;font-size:16.5px;line-height:20px;}
  .answer-text{font-style:italic;font-size:11.1px;line-height:20px;white-space:nowrap;}

  .sources{position:absolute;left:0;width:750px;top:1122px;text-align:center;font-family:"Noto Serif",serif;font-weight:700;font-size:8.8px;color:var(--white);}
  .page-tab{position:absolute;left:800px;top:1123px;width:24px;height:40px;border:2px solid var(--pink);border-bottom:none;border-radius:12px 12px 0 0;font-family:"Noto Serif",serif;font-weight:700;font-size:13px;color:var(--ink);text-align:center;padding-top:6px;}
</style>
</head>
<body>
<div class="canvas">
  <svg class="art" width="912" height="1200" viewBox="0 0 912 1200" aria-hidden="false">
    <defs>
      <linearGradient id="navyFill" x1="0" y1="0" x2="0" y2="1">
        <stop offset="0" stop-color="#1a2c58"/>
        <stop offset="1" stop-color="#0e1836"/>
      </linearGradient>
      <linearGradient id="warmBlend" x1="0" y1="0" x2="1" y2="0">
        <stop offset="0" stop-color="var(--pink)"/>
        <stop offset="1" stop-color="var(--orange)"/>
      </linearGradient>
      <linearGradient id="photoTone" x1="0" y1="0" x2="0.4" y2="1">
        <stop offset="0" stop-color="#cfe3f2"/>
        <stop offset="0.4" stop-color="#b9c3cf"/>
        <stop offset="0.75" stop-color="#6f7784"/>
        <stop offset="1" stop-color="#1c2540"/>
      </linearGradient>
      <linearGradient id="bodyTone" x1="0" y1="0" x2="1" y2="0">
        <stop offset="0" stop-color="#7c828d"/>
        <stop offset="0.6" stop-color="#4a5163"/>
        <stop offset="1" stop-color="#16213f" stop-opacity="0"/>
      </linearGradient>
    </defs>

    <!-- front side -->
    <rect x="58" y="45" width="803" height="551" fill="url(#navyFill)"/>
    <rect x="58" y="300" width="300" height="296" fill="url(#bodyTone)" role="img" aria-label="Photo of a smiling doctor holding her abdomen with a glowing digestive tract overlay"/>
    <path d="M670 45 L861 45 L861 128 C845 140 840 130 820 118 C790 100 760 120 735 100 C712 82 690 72 670 45 Z" fill="url(#warmBlend)"/>
    <path d="M58 271 C100 300 150 340 200 336 C250 332 270 290 300 245 C285 305 230 350 160 345 C110 342 80 320 58 300 Z" fill="var(--pink)"/>
    <path d="M300 245 C340 180 400 170 415 100 C420 150 395 200 330 225 Z" fill="var(--orange)"/>
    <path d="M58 45 L415 45 C412 110 390 160 340 185 C300 205 275 240 250 280 C220 325 170 345 120 315 L58 270 Z" fill="url(#photoTone)" stroke="var(--white)" stroke-width="3" role="img" aria-label="Photo of a smiling female doctor in a white coat with stethoscope"/>
    <circle cx="416" cy="77" r="15" fill="var(--coral)"/>
    <circle cx="325" cy="322" r="15" fill="#c85a86"/>
    <path d="M630 596 C670 578 730 578 770 596 Z" fill="var(--orange)"/>

    <!-- back side -->
    <rect x="58" y="613" width="803" height="550" fill="var(--paper)"/>
    <path d="M58 685 C130 650 220 645 300 668 C380 690 440 690 530 614 L842 614 L861 636 L861 880 C830 915 800 935 770 955 L700 1108 L628 1163 L173 1163 L58 1060 Z" fill="url(#warmBlend)"/>
  </svg>

  <!-- front side text -->
  <div class="watermark">Gastro</div>
  <h1 class="card-subject">Gastrointestinal</h1>
  <div class="case-id">PATHOLOGY CASE ID 0001</div>
  <p class="case-stem">
    50-year-old woman comes to the clinic because she has<br>
    difficulty swallowing for the past few months.&nbsp; She says<br>
    symptoms have been worsening.&nbsp; She also complains of<br>
    cough, mostly at night and in fear of choking, has stopped<br>
    eating many foods, losing about 12 lbs in the past 3 months.<br>
    Past medical history is unremarkable. Vital signs are normal<br>
    and physical exam is unremarkable.&nbsp; Chest x-ray with<br>
    demonstrates an air-fluid level, while manometry shows<br>
    absent relaxation of the lower esophageal sphincter during<br>
    swallowing.&nbsp; What is the most likely diagnosis?
  </p>
  <div class="divider"></div>
  <div class="options">
    <span class="opt"><span class="letter">A)</span> GERD</span>
    <span class="opt"><span class="letter">B)</span> Barret Esophagus</span>
    <span class="opt"><span class="letter">C)</span> Achalasia</span><br>
    <span class="opt"><span class="letter">D)</span> Eosinophilic esophagitis</span>
  </div>

  <!-- back side text -->
  <h2 class="back-text topic-title">Achalasia</h2>
  <p class="back-text section definition"><b>Definition:</b> •Motility disorder where esophageal relaxation is impaired in the lower esophageal sphincter (LES).</p>
  <p class="back-text section etiology"><span class="label-block">Etiology/Pathology:</span>Destruction of inhibitory neurons in the Auerbach plexus.<br>Loss of peristalsis in the lower esophageal sphincter<br>(Lower-two thirds of the esophagus).</p>
  <p class="back-text section symptoms"><b>P/E and Symptoms</b>•Dysphagia that is progressive, regurgitation, weight-loss, dry cough, chest pain, GERD, esophageal perforation, squamous cell carcinoma, aspiration pneumonia.</p>
  <p class="back-text section diagnosis"><span class="label-block">Dx:</span>&nbsp;•Barium swallow will show ‘bird’s beak’ and esophageal dilation. Manometry will present with increased resting lower esophageal sphincter pressure. Endoscopy will usually present with normal mucosa and LES dilation, and in some cases residual material such as undigested food particles may be present.</p>
  <p class="back-text section treatment"><b>Rx:</b>&nbsp; First line of treatment are nitrates, calcium channel blockers, and Botulinum toxin injection in the LES.&nbsp; Long term management options include esophageal dilation with pneumatic balloon and myotomy.</p>

  <div class="answer-box">
    <h3 class="answer-title">C- Achalasia</h3>
    <p class="answer-text">
      Symptoms and studies suggestive of achalasia.&nbsp; Patient’s manometry presents with no relaxation of the lower esophageal<br>
      sphincter during swallowing.&nbsp; Patient also complains of dysphagia and is unable to swallow properly, leading to weight loss.<br>
      Patient has no past infection or inflammation, ruling out eosinophilic esophagitis.&nbsp; Patient does not have chronic GERD,<br>
      eliminating the possibility of Barrett esophagus, in which at least 5 years of acid reflux are beforehand to develop columnar<br>
      metaplasia.
    </p>
  </div>

  <p class="sources">Sources: Halvern Drug Guide | Pocket Formulary Review | Medirefs.net | Clinipedia.org</p>
  <div class="page-tab">1</div>
</div>
</body>
</html>
```